Taking a Paper and turning into a wonderful White Paper for Prospects and Clients

This is a white paper I need designed. I am including my company brochure so you can see the design/fonts being used and I'm including a white paper created - one that I like very much.

I am "NOT" looking for a cookie cutter white paper. I'm looking for a nice, clean design but with some creativity. Check out the white paper I included and you will get the idea.

Also included:
- the paper to be designed
- the paper to be designed "WITH" suggested design features such as carve outs, call outs and such

A few things I "DO NOT" like:
- images that are cheesy or corny
* people sitting at a table in a meeting
* Buildings

The white paper I included did not use pictures but had more design created by the firm. I like this approach and will probably give something like this more weight but is not required.

Reason: Realized time frame was too tight

Target Market(s)

Higher-End, wealthier clients

Industry/Entity Type

It Company

Requirements
Must have
• I DO NOT want the copy to be bunched together. The layout should flow where the copy is broken in the right spots to make reading easier. If you read a paper and it is just copy, interest is lost by everyone.
• COLORS: you can see from what I have included the colors I use
• My preference are very balanced colors using "clean spacing"

```html
<!DOCTYPE html>
<html lang="en">
<head>
<meta charset="utf-8">
<title>Veravia White Paper</title>
<link href="https://fonts.googleapis.com/css2?family=Montserrat:wght@400;500;600;700&family=Source+Serif+4:ital,opsz,wght@0,8..60,400;0,8..60,600;1,8..60,400&display=swap" rel="stylesheet">
<style>
:root{
  --green:#3db35f;
  --red:#e2323f;
  --navy:#16264f;
  --teal:#a6dedd;
  --ink:#1f1f24;
  --muted:#55575c;
  --paper:#ffffff;
  --stage:#ffffff;
}
*{box-sizing:border-box;margin:0;padding:0}
html,body{width:944px;height:1200px;overflow:hidden;background:var(--stage)}
body{position:relative;font-family:"Source Serif 4",Georgia,serif;color:var(--ink)}
.page{position:absolute;width:432px;height:558px;background:var(--paper);box-shadow:0 3px 14px rgba(0,0,0,.18);overflow:hidden}
.page--1{left:21px;top:21px}
.page--2{left:467px;top:21px}
.page--3{left:21px;top:594px}
.page--4{left:467px;top:594px}
.page::after{content:"";position:absolute;left:0;right:0;bottom:0;height:10px;background:var(--navy)}
.brand{position:absolute;left:26px;top:14px;font-family:"Montserrat",sans-serif;font-weight:500;font-size:15px;letter-spacing:1px;color:var(--navy)}
.site{position:absolute;left:26px;top:517px;font-family:"Montserrat",sans-serif;font-weight:600;font-size:10px;color:var(--navy)}
.abs{position:absolute}
.body-copy p{font-size:7.5px;line-height:10.7px;margin-bottom:4.5px}
.body-copy b{font-weight:600}
.label{font-family:"Montserrat",sans-serif;font-weight:600;font-size:8px;letter-spacing:1.8px;text-transform:uppercase}
.label--red{color:var(--red)}
.label--green{color:var(--green)}
.sublabel{font-family:"Montserrat",sans-serif;font-weight:500;font-size:6.3px;letter-spacing:1.3px;color:var(--ink);margin-top:4px;text-transform:uppercase}
.note{font-style:italic;font-size:7.2px;line-height:10.4px;color:var(--muted)}
.lead-red{color:var(--red);font-family:"Montserrat",sans-serif;font-size:6.6px;font-weight:500}
.tag{color:var(--green);font-family:"Montserrat",sans-serif;font-size:5.8px;font-weight:600;letter-spacing:.6px;text-transform:uppercase}

/* page 1 */
.banner{left:26px;top:93px;width:381px;height:62px;background:var(--green);color:#fff;font-family:"Montserrat",sans-serif;font-weight:600;font-size:13.6px;line-height:25px;padding:7px 11px}
.banner-fold{left:386px;top:155px}
.intro{left:68px;top:182px;width:260px;color:var(--green);font-family:"Montserrat",sans-serif;font-weight:500;font-size:9.4px;line-height:12px}
.intro p{margin-bottom:8px}
.sources{left:68px;top:256px;width:120px;font-family:"Montserrat",sans-serif;font-size:5.4px;line-height:8.6px;color:var(--muted)}
.sources p{margin-bottom:2px}
.sources .link{display:block;margin:4px 0 2px}
.col-right{left:197px;width:200px}

/* page 2 */
.pull{left:26px;top:306px;width:140px;color:var(--green);font-family:"Montserrat",sans-serif;font-weight:400;font-size:12px;line-height:15px}

/* page 3 */
.head-l{left:26px;top:62px}
.head-r{left:197px;top:62px}
.cell{position:absolute}
.cell--red{background:var(--red);color:#fff;font-family:"Montserrat",sans-serif;font-size:7.4px;line-height:10px;padding:11px 12px}
.cell--teal{background:var(--teal);font-style:italic;color:#26323a;font-size:7.4px;line-height:10px;padding:10px 9px}
.cell--teal p{margin-bottom:5.5px}

/* page 4 */
.contact{left:26px;top:368px;font-family:"Montserrat",sans-serif;font-size:9.6px;color:var(--navy)}
.contact div{display:flex;align-items:center;gap:4px;margin-bottom:4px}
.checks li{list-style:none;font-family:"Montserrat",sans-serif;font-size:6.8px;line-height:9.4px;font-weight:500;display:flex;gap:3px;align-items:flex-start;margin-bottom:4px}
.brand-big{left:250px;top:494px;width:160px;text-align:right;font-family:"Montserrat",sans-serif;font-weight:500;color:var(--navy)}
.brand-big .name{font-size:21px;letter-spacing:1.5px;display:block}
.brand-big .motto{font-size:6px;letter-spacing:.8px}
</style>
</head>
<body>

<section class="page page--1">
  <div class="brand">VERAVIA</div>
  <h1 class="abs banner">Is your financial advisor a fiduciary?<br>Is not that simple...</h1>
  <svg class="abs banner-fold" width="21" height="16" viewBox="0 0 21 16"><path d="M0 0H21V16Z" fill="var(--green)"/></svg>
  <div class="abs intro">
    <p>Well, we say, the question is not whether your financial advisor is a fiduciary.</p>
    <p>The question is whether your financial advisor is consistently acting in your best interest.</p>
  </div>
  <div class="abs sources">
    <p>From MARKET LEDGER,<br>by Lawrence Stahl:<br>“Why Your Financial Advisor<br>Should Be A Fiduciary”</p>
    <svg class="link" width="8" height="8" viewBox="0 0 8 8"><path d="M3 1H1v6h6V5M4.5 1H7v2.5M7 1 3.5 4.5" fill="none" stroke="#2a8ed8" stroke-width=".9"/></svg>
    <p>From PUBLIC EVENING REPORT,<br>by Harold Pell:<br>“Why you should make sure your<br>financial advisor abides by the<br>fiduciary standard”</p>
  </div>
  <div class="abs col-right body-copy" style="top:256px">
    <p>As an investor, you’ve almost certainly heard talk about the differences between “the fiduciary standard” and “the suitability standard,” applied—varyingly—to advisers, brokers and other financial professionals.</p>
    <p>In fact, most likely you’ve heard it said— umpteen times—that unless your financial advisors are fiduciaries, required by law to adhere to the fiduciary standard, they won’t consistently act with your best interests in mind.</p>
    <p>Nonetheless, some investors may, for any number of reasons, still choose to hire professionals who work under the suitability standard.</p>
    <p>But, the question remains, <b>should you only hire an advisor acting as a fiduciary and avoid those who are not?</b></p>
    <p>Here at Veravia—where we audit advisors for our clients covering areas such as fees charged, performance delivered, and investments used—we make certain our clients have great advisors.</p>
    <p>But, our paramount demand, made of all the advisors we audit is—the Financial Advisor “acts in our client’s best interest.”</p>
  </div>
  <div class="site">veravia.com</div>
</section>

<section class="page page--2">
  <div class="brand">VERAVIA</div>
  <div class="abs" style="left:26px;top:63px;width:140px">
    <div class="label label--red">A Cautionary Tale</div>
    <p class="note" style="margin-top:10px">This story illustrates some eventual pitfalls of choosing financial advisors based solely on whether they work under the fiduciary standard.</p>
  </div>
  <p class="abs pull">Veravia proactively verifies that your financial advisors are consistently acting in your best interest.</p>
  <div class="abs col-right body-copy" style="top:63px;width:200px">
    <p><span class="lead-red">Three sports stars:</span> professional baseball pitchers <b>Ray Ostrand</b> and <b>Jake Pelley</b>, and pro football quarterback <b>Mark Salcedo</b> believed they were bringing their “A-game” to the search for a great, trustworthy financial advisor.</p>
    <p>Ashok Nairn, the financial advisor they chose, seemed to be made of all the right stuff. He worked for the Dallas-based KDL Wealth Advisors. According to his business bios and cards, he was a Certified Public Account. The National Football Players’ Guild had endorsed him. Furthermore, he regularly attended the same church as Salcedo and had an interest in charity work.</p>
    <p>Ashok Nairn, nonetheless, turned out to be ruinously unscrupulous. He was not, in fact, a CPA. By fraudulent means, he transferred money out of his clients’ accounts, often without their consent, into The Seat Exchange, a financially-distressed company. And as a Seat Exchange board member, Nairn had multiple, egregious conflicts of interest that he never disclosed to his clients. By the time the deceitful scheme was uncovered and stopped, Nairn had misdirected $33 million of the three athletes’ money and nearly all of it was lost.</p>
    <p><span class="lead-red">One crucial fact</span> got left out of most of the reporting on that story, namely, that Ashok Nairn was a fiduciary.</p>
    <p>As a Registered Investment Advisor working through KDL Capital Management, Nairn was legally required to put his clients’ interests before his own and to act in their best interests. He failed to do that. Subsequently, the federal securities regulator’s case against him was settled without his clients being fully reimbursed.</p>
    <p><span class="lead-red">Was this avoidable?</span> Veravia tells you “Yes, this was avoidable.” What happened to Mark Salcedo does not have to happen to you. Veravia pro-actively verifies that your financial advisors are consistently acting in your best interest.</p>
    <p>The fine points in the differences between “the fiduciary standard” and “the suitability standard” are important for all of us to know, to be sure, but what’s most important for now is to understand that the mere fact of an adviser being a fiduciary does not guarantee that the adviser will do the right things for you.</p>
  </div>
  <div class="site">veravia.com</div>
</section>

<section class="page page--3">
  <div class="brand">VERAVIA</div>
  <div class="abs head-l"><div class="label label--red">A Cautionary Tale</div><div class="sublabel">Problem with Nairn</div></div>
  <div class="abs head-r"><div class="label label--red">Protective Measures</div><div class="sublabel">Veravia’s steps to protect you</div></div>

  <div class="cell cell--red" style="left:26px;top:88px;width:169px;height:60px">Nairn misrepresented himself as a CPA, but was not one.</div>
  <div class="cell cell--teal" style="left:198px;top:88px;width:209px;height:60px">
    <p>We perform thoroughgoing background checks for every single credential an advisor claims.</p>
    <p>We thoroughly verify claims about both educational background and professional certifications.</p>
  </div>
  <div class="cell cell--red" style="left:26px;top:151px;width:169px;height:361px">Nairn improperly diverted Salcedo’s funds.</div>
  <div class="cell cell--teal" style="left:198px;top:151px;width:209px;height:361px">
    <p>We obtain your account statements showing assets held, and any transfers.</p>
    <p>In Salcedo’s case, we would have seen the transfers to The Seat Exchange, and then verified with Salcedo that he had authorized those transfers for the reported amounts.</p>
    <p>Additionally, when an advisor makes outside investments for our clients, we do deeper dives.</p>
    <p>Why was the investment bought? Who has control of the investment? How are the assets valued and audited?</p>
    <p>We answer those kinds of questions. We can clearly explain to you why we posed each question and what we think of the answer.</p>
    <p>We would have been evaluating how KDL Capital’s management structure provides oversight and auditing of what its advisors are doing for their clients.</p>
    <p>Whatever the source of such an endorsement—be it a players’ association, a listing in the Global Finance Daily Top 400, or Barrow’s Weekly Top 100 Advisors, etc.—we view it with great skepticism.</p>
    <p>Why?</p>
    <p>These organizations base their advisor rankings on limited metrics such as the number of years an advisor has been in the industry and the types of clients the advisor has.</p>
    <p>Those metrics are of small import for an individual investor. Such limited metrics comprise less than 10% of what Veravia looks at when evaluating financial advisors.</p>
  </div>
  <div class="site">veravia.com</div>
</section>

<section class="page page--4">
  <div class="abs" style="left:26px;top:63px;width:142px">
    <div class="label label--green">Who are we?</div>
    <p class="note" style="margin-top:9px;color:var(--ink)">We are VERAVIA—a client advocacy firm working on behalf of our clients to make certain they have hired, or will hire, a great financial advisor.</p>
    <p class="note" style="margin-top:4px;color:var(--ink)">With over 600,000 registered advisors in the United States, how do you know the advisor you might choose is one of the best?</p>
  </div>
  <div class="abs label" style="left:26px;top:300px;color:var(--ink);font-size:7.4px;line-height:13px">Discover<br>the Veravia difference</div>
  <div class="abs contact">
    <div><svg width="12" height="12" viewBox="0 0 12 12"><circle cx="6" cy="6" r="6" fill="var(--navy)"/><rect x="2.8" y="3.8" width="6.4" height="4.4" fill="none" stroke="#fff" stroke-width=".8"/><path d="M2.8 3.8 6 6.4 9.2 3.8" fill="none" stroke="#fff" stroke-width=".8"/></svg>mail@veravia.com</div>
    <div><svg width="12" height="12" viewBox="0 0 12 12"><circle cx="6" cy="6" r="6" fill="var(--navy)"/><path d="M4.3 3c.5 2.5 2 4.2 4.4 5.2l-.9 1C5 8 3.5 6 3.2 3.6Z" fill="#fff"/></svg>555–014–2290</div>
  </div>

  <div class="abs col-right body-copy" style="top:63px;width:200px">
    <p>We have <b>four core areas</b> clients entrust us to help:</p>
    <p><span class="tag">Evaluate</span> your current financial advisor in 16+ areas; fee’s being charged, investment returns, investment products being used, background check on the advisor and firm, to name a few</p>
    <p><span class="tag">Find</span> a great financial advisor with a customized search based on your needs and goals but making certain the advisor delivers good, risk-based returns for a fair fee</p>
    <p><span class="tag">Performance Guard</span> focused on periodic check-ups on your investments and returns. We provide you comfort in knowing your advisors is investing correctly, with the right products and the right fees.</p>
    <p><span class="tag">Advisor Background Check</span> helps you understand who you are working with currently or who you might hire; do they have the right experience, client complaints or fines, are they truthful in what they said about education, credentials, and background? We verify this information on behalf of our clients.</p>
  </div>
  <div class="abs col-right body-copy" style="top:300px;width:200px">
    <p>When working on your behalf we audit the Registered Investment Advisors, Wealth Managers, Private Bankers, Trust Officers, Brokers or whatever other titles the financial professional may have, what concerns us is that they:</p>
    <ul class="checks">
      <li><svg width="10" height="8" viewBox="0 0 10 8"><path d="M1 4 3.8 6.8 9 1" fill="none" stroke="var(--green)" stroke-width="1.8"/></svg>Be honest with you</li>
      <li><svg width="10" height="8" viewBox="0 0 10 8"><path d="M1 4 3.8 6.8 9 1" fill="none" stroke="var(--green)" stroke-width="1.8"/></svg>Provide you with sound advice</li>
      <li><svg width="10" height="8" viewBox="0 0 10 8"><path d="M1 4 3.8 6.8 9 1" fill="none" stroke="var(--green)" stroke-width="1.8"/></svg>Look out for your best interest</li>
    </ul>
    <p style="margin-top:3px">Offer advice for a fair fee, “or” fair compensation;</p>
    <p>and then, above all;</p>
    <ul class="checks">
      <li><svg width="10" height="8" viewBox="0 0 10 8" style="flex:none"><path d="M1 4 3.8 6.8 9 1" fill="none" stroke="var(--green)" stroke-width="1.8"/></svg><span>We must be able to verify that your advisors<br>are consistently doing the right things for you.</span></li>
    </ul>
  </div>
  <div class="abs brand-big"><span class="name">VERAVIA</span><span class="motto">CLARITY FOR EVERY CLIENT</span></div>
  <div class="site">veravia.com</div>
</section>

</body>
</html>
```